Bottle label design for a mulberry brandy

Please create a label design for a mulberry brandy. The registered brand name is "Kolvat"
The brandy will be produced in Armenia from 100% mulberry.
Color of the product: transparent.
The product will be sold worldwide. The price will be between 30 and 50 USD. So the product will be in premium category.
Therefore we need a solid design, appropriate to the product price category. The design, however, needs to be modern and optimistic.
You can have mulberries on the label or not have, it is up to you.
We have chosen for the product some bottle types, the links to the available bottles you can find in the attachment. Ideally you show a picture of your label on the bottle you selected.

Target Market(s)

worldwide

```html
<!DOCTYPE html>
<html lang="en">
<head>
<meta charset="utf-8">
<title>Kolvat Premium – Mulberry Brandy Label</title>
<link rel="stylesheet" href="https://fonts.googleapis.com/css2?family=Rye&family=Oswald:wght@400;500&display=swap">
<style>
  :root {
    --backdrop: #dcdcdc;
    --label-ink: #231d1e;
    --grain-dark: #141112;
    --grain-light: #3a3435;
    --cream: #f6f1e4;
    --gold-light: #f1d57e;
    --gold-mid: #c9a24a;
    --gold-dark: #8a6424;
    --ribbon-text: #2b2016;
    --gold-text: #e8d27a;
  }
  html, body {
    margin: 0;
    width: 1200px;
    height: 1200px;
    overflow: hidden;
    background: radial-gradient(circle at 50% 40%, #f2f2f2 0%, var(--backdrop) 75%);
  }
  .label {
    position: absolute;
    left: 327px;
    top: 50px;
    width: 545px;
    height: 1100px;
    display: block;
  }
  .brand-name {
    font-family: "Rye", serif;
    fill: var(--cream);
  }
  .ribbon-text {
    font-family: "Oswald", sans-serif;
    font-weight: 500;
    fill: var(--ribbon-text);
  }
  .origin-text {
    font-family: "Oswald", sans-serif;
    font-weight: 400;
    fill: var(--gold-text);
  }
  .volume-text {
    font-family: "Oswald", sans-serif;
    font-weight: 400;
    fill: var(--cream);
  }
</style>
</head>
<body>
<svg class="label" viewBox="0 0 545 1100" xmlns="http://www.w3.org/2000/svg">
  <defs>
    <linearGradient id="grain-fill" x1="0" y1="0" x2="1" y2="1">
      <stop offset="0" stop-color="var(--grain-light)"/>
      <stop offset="0.5" stop-color="var(--grain-dark)"/>
      <stop offset="1" stop-color="var(--grain-light)"/>
    </linearGradient>
    <linearGradient id="gold-fill" x1="0" y1="0" x2="1" y2="0">
      <stop offset="0" stop-color="var(--gold-dark)"/>
      <stop offset="0.3" stop-color="var(--gold-light)"/>
      <stop offset="0.6" stop-color="var(--gold-mid)"/>
      <stop offset="1" stop-color="var(--gold-light)"/>
    </linearGradient>
    <radialGradient id="fruit-fill" cx="0.5" cy="0.5" r="0.6">
      <stop offset="0" stop-color="#d9d3c4"/>
      <stop offset="1" stop-color="#4a4344"/>
    </radialGradient>
  </defs>

  <rect class="label-base" width="545" height="1100" fill="var(--label-ink)"/>

  <rect class="grain-panel" x="31" y="38" width="481" height="492" fill="url(#grain-fill)"
        role="img" aria-label="Flowing wood-grain line pattern"/>

  <text class="brand-name" x="272" y="500" text-anchor="middle" font-size="190"
        textLength="411" lengthAdjust="spacingAndGlyphs">KOLVAT</text>

  <g class="ribbon">
    <polygon points="0,0 0,0" />
    <polygon points="57,560 115,545 120,605 67,621 85,588" fill="var(--gold-dark)"/>
    <polygon points="481,560 423,545 418,605 471,621 453,588" fill="var(--gold-dark)"/>
    <path d="M95,530 Q272,495 449,530 L449,585 Q272,550 95,585 Z" fill="url(#gold-fill)"/>
    <text class="ribbon-text" x="272" y="566" text-anchor="middle" font-size="50"
          textLength="174" lengthAdjust="spacingAndGlyphs">PREMIUM</text>
  </g>

  <rect class="fruit-illustration" x="88" y="612" width="411" height="269" rx="120"
        fill="url(#fruit-fill)" role="img" aria-label="Engraved illustration of two mulberries with a leaf"/>

  <rect class="grain-band" x="31" y="901" width="481" height="73" fill="url(#grain-fill)"
        role="img" aria-label="Band of flowing wood-grain line pattern"/>

  <text class="origin-text" x="271" y="1011" text-anchor="middle" font-size="18"
        textLength="96" lengthAdjust="spacingAndGlyphs">100% MULBERRY</text>
  <text class="volume-text" x="38" y="1061" font-size="40"
        textLength="68" lengthAdjust="spacingAndGlyphs">70 cl</text>
  <text class="origin-text" x="139" y="1061" font-size="42"
        textLength="265" lengthAdjust="spacingAndGlyphs">PRODUCED IN ARMENIA</text>
</svg>
</body>
</html>
```